Dr. Calvin Ostrander personal brand website

I need a new website for a client who is in a speaker, author, and consultant in the mental health space.

Dr. Ostrander is a mental healthcare speaker, author, coach, and consultant who has worked with clients at the local and state levels.

His website will be used to market him for speaking and media opportunities, as well as to inform potential consulting clients.

Included with the uploaded files is a brand strategy document that outlines how Dr. Ostrander's personal brand will be positioned in the marketplace.

Examples of websites to draw inspiration from:
https://www.petraquillon.com
https://drmarcotervaine.com
http://janetorvik.com/

Pages:
Meet The Doctor (bio is included with uploaded files)
The Book (picture of the book is included)
Speaking
Consulting (include link to https://kvtmwro.com/)
Contact

Target Market(s)

Mental Health/Substance Abuse Recovery

Industry/Entity Type

Mental Health

Coding

Coded - Design and coding required

Number of Pages Required

5+ page

Font styles to use
Sans Serif

Colors

Designer to choose colors to be used in the design.

Requirements
Must have
• Popup optin form to capture email addresses.
Should not have
• no clipart or stock images

```html
<!DOCTYPE html>
<html lang="en">
<head>
<meta charset="utf-8">
<title>Speaking – Dr. Calvin Ostrander</title>
<link href="https://fonts.googleapis.com/css2?family=Roboto:wght@300;400;500;700;900&display=swap" rel="stylesheet">
<style>
  :root {
    --backdrop: #e4e4e4;
    --page: #ffffff;
    --brand-blue: #0172c2;
    --navy: #01204a;
    --black: #000000;
    --text: #111111;
    --hairline: #9a9a9a;
    --wall-light: #f1f1f1;
    --wall-mid: #d6d6d6;
  }
  * { margin: 0; padding: 0; box-sizing: border-box; }
  html, body { width: 1200px; height: 1200px; overflow: hidden; }
  body { background: var(--backdrop); font-family: "Roboto", sans-serif; position: relative; }
  .page { position: absolute; left: 295px; top: 4px; width: 602px; height: 1196px; background: var(--page); overflow: hidden; }
  .abs { position: absolute; }

  /* top strip */
  .topbar { left: 0; top: 0; width: 602px; height: 13px; border-bottom: 1px solid #eee; }
  .social-dot { width: 6px; height: 6px; border-radius: 50%; background: #4a8fd0; top: 4px; }
  .schedule { right: 38px; top: 3px; font-size: 5.5px; color: var(--brand-blue); display: flex; align-items: center; gap: 3px; }
  .schedule svg { width: 7px; height: 7px; }

  /* header */
  .logo-mark { left: 50px; top: 14px; width: 30px; height: 30px; border-radius: 50%; background: var(--brand-blue); }
  .logo-name { left: 36px; top: 45px; width: 60px; font-size: 5.5px; font-weight: 500; color: var(--navy); text-align: center; white-space: nowrap; }
  .search { left: 273px; top: 26px; width: 171px; height: 17px; border: 1px solid #cfcfcf; border-radius: 2px; font-size: 5px; color: #888; padding: 5px 7px; }
  .search svg { position: absolute; right: 6px; top: 4px; width: 9px; height: 9px; }
  .btn-call { left: 454px; top: 20px; width: 111px; height: 13px; background: var(--black); color: #fff; font-size: 5.5px; font-weight: 700; text-align: center; line-height: 13px; border-radius: 1px; }
  .btn-book { left: 454px; top: 37px; width: 111px; height: 13px; background: var(--brand-blue); color: #fff; font-size: 5.5px; font-weight: 700; text-align: center; line-height: 13px; border-radius: 1px; }

  /* navigation */
  .nav { left: 0; top: 53px; width: 602px; height: 24px; background: var(--brand-blue); }
  .nav-item { top: 0; height: 24px; line-height: 23px; font-size: 6px; font-weight: 700; color: #fff; letter-spacing: 0.1px; }
  .nav-item.active { color: #d9ebff; font-weight: 500; }
  .nav-underline { left: 201px; top: 75px; width: 51px; height: 2px; background: var(--navy); }

  /* hero */
  .hero { left: 0; top: 77px; width: 602px; height: 206px;
    background: linear-gradient(180deg, var(--wall-light) 0%, #e8e8e8 55%, var(--wall-mid) 82%, #ececec 100%); }
  .hero-floor { left: 0; top: 261px; width: 602px; height: 22px; background: linear-gradient(180deg, #dcdcdc, #f3f3f3); }
  .hero-title { left: 48px; top: 100px; font-size: 16.5px; font-weight: 700; color: var(--brand-blue); letter-spacing: 0.2px; }
  .hero-copy { left: 48px; top: 131px; width: 258px; font-size: 11px; line-height: 13.6px; color: var(--text); }
  .btn-read { left: 48px; top: 246px; width: 74px; height: 16px; background: var(--navy); color: #fff; font-size: 5.5px; font-weight: 700; text-align: center; line-height: 16px; border-radius: 1px; }
  .frame-band { left: 449px; width: 153px; height: 12px; background: var(--brand-blue); }
  .hero-photo { left: 417px; top: 92px; width: 185px; height: 176px;
    background: linear-gradient(135deg, #c9d2dd 0%, #e3e6ea 40%, #3a3f4c 60%, #cfd4da 100%);
    box-shadow: -8px 0 8px rgba(0,0,0,0.35); }

  /* section headings */
  .section-title { left: 0; width: 602px; text-align: center; font-size: 14px; color: var(--brand-blue); font-weight: 400; }
  .section-title strong { font-weight: 700; }
  .section-rule { left: 278px; width: 42px; height: 2px; background: var(--navy); }

  /* seminar panel */
  .seminar { left: 36px; top: 347px; width: 530px; height: 256px; background: var(--brand-blue); color: #fff; }
  .seminar h3 { position: absolute; left: 0; top: 24px; width: 530px; text-align: center; font-size: 12.5px; font-weight: 700; }
  .seminar p { position: absolute; left: 130px; width: 270px; text-align: center; font-size: 7px; line-height: 12.7px; font-weight: 400; }

  /* topic cards */
  .card { display: flex; flex-direction: column; align-items: center; text-align: center; }
  .card-dark { background: var(--navy); }
  .card-light { background: #fff; border: 1px solid var(--hairline); }
  .card h4 { font-weight: 900; letter-spacing: 0.2px; }
  .card-dark h4 { color: #fff; font-size: 20.5px; }
  .card-light h4 { color: var(--brand-blue); font-size: 20.5px; }
  .card p { font-size: 10.5px; font-weight: 500; line-height: 21.8px; }
  .card-dark p { color: var(--brand-blue); }
  .card-light p { color: var(--navy); }

  /* video band */
  .video-band { left: 0; top: 1080px; width: 602px; height: 116px; background: var(--brand-blue); }
  .outline-left { left: 110px; top: 1096px; width: 80px; height: 110px; border: 1px solid rgba(255,255,255,0.8); border-right: none; }
  .outline-right { left: 407px; top: 1096px; width: 87px; height: 110px; border: 1px solid rgba(255,255,255,0.8); border-left: none; }
  .video-frame { left: 188px; top: 1058px; width: 219px; height: 150px; background: var(--brand-blue); }
  .video-still { left: 192px; top: 1062px; width: 211px; height: 140px;
    background: linear-gradient(160deg, #4a4f57 0%, #26282d 45%, #5b5a58 75%, #8c8880 100%); }
  .play { left: 275px; top: 1135px; width: 46px; height: 46px; }
  .arrow { width: 16px; height: 24px; top: 1145px; }
</style>
</head>
<body>
<div class="page">

  <!-- top strip -->
  <div class="abs topbar"></div>
  <div class="abs social-dot" style="left:36px"></div>
  <div class="abs social-dot" style="left:50px"></div>
  <div class="abs social-dot" style="left:64px"></div>
  <div class="abs schedule">
    <svg viewBox="0 0 10 10"><rect x="1" y="2" width="8" height="7" fill="none" stroke="#222" stroke-width="1"/><line x1="1" y1="4" x2="9" y2="4" stroke="#222"/><line x1="3" y1="1" x2="3" y2="3" stroke="#222"/><line x1="7" y1="1" x2="7" y2="3" stroke="#222"/></svg>
    Schedule an Appointment
  </div>

  <!-- header -->
  <div class="abs logo-mark"></div>
  <div class="abs logo-name">Dr. Calvin Ostrander</div>
  <div class="abs search">Search here...
    <svg viewBox="0 0 10 10"><circle cx="4" cy="4" r="3" fill="none" stroke="#555" stroke-width="1"/><line x1="6.2" y1="6.2" x2="9.2" y2="9.2" stroke="#555" stroke-width="1"/></svg>
  </div>
  <div class="abs btn-call">CALL US TODAY: 000-111-1111</div>
  <div class="abs btn-book">BOOK NOW DR. CALVIN OSTRANDER</div>

  <!-- navigation -->
  <div class="abs nav">
    <span class="abs nav-item" style="left:45px">HOME</span>
    <span class="abs nav-item" style="left:81px">MEET THE DOCTOR</span>
    <span class="abs nav-item" style="left:158px">THE BOOK</span>
    <span class="abs nav-item active" style="left:212px">SPEAKING</span>
    <span class="abs nav-item" style="left:266px">CONSULTING</span>
    <span class="abs nav-item" style="left:330px">CONTACT</span>
  </div>
  <div class="abs nav-underline"></div>

  <!-- hero -->
  <div class="abs hero"></div>
  <div class="abs hero-floor"></div>
  <h1 class="abs hero-title">SPEAKING</h1>
  <p class="abs hero-copy">Knowing the person behind the creation of Harborlight Behavioral Health Services is important.&nbsp; Not only to the Consumers who attend many of our programs and services but, to those who are apart of the Maple Crest Community.&nbsp; When Programs are erected in our Communities most people do.</p>
  <div class="abs btn-read">READ MORE</div>
  <div class="abs frame-band" style="top:80px"></div>
  <div class="abs frame-band" style="top:268px"></div>
  <div class="abs hero-photo" role="img" aria-label="Photo of Dr. Ostrander speaking to a seated audience in a bright room"></div>

  <!-- seminars -->
  <h2 class="abs section-title" style="top:306px"><strong>DR. CALVIN OSTRANDER</strong> SEMINARS &amp; WORKSHOPS</h2>
  <div class="abs section-rule" style="top:328px"></div>

  <div class="abs seminar">
    <h3>Prevent burnout and live more resilient lives.</h3>
    <p style="top:57px">Lorem ipsum dolor sit amet, consectetur adipiscing elit, sed do eiusmod tempor incididunt ut labore et dolore magna aliqua. Ut enim ad minim veniam, quis nostrud exercitation ullamco laboris nisi ut aliquip ex ea commodo consequat. Duis aute irure dolor in reprehenderit in voluptate velit esse cillum dolore eu fugiat nulla pariatur. Excepteur sint occaecat cupidatat non proident, sunt in culpa qui officia deserunt mollit anim id est laborum.</p>
    <p style="top:146px">Lorem ipsum dolor sit amet, consectetur adipiscing elit, sed do eiusmod tempor incididunt ut labore et dolore magna aliqua. Ut enim ad minim veniam, quis nostrud exercitation ullamco laboris nisi ut aliquip ex ea commodo consequat. Duis aute irure dolor in reprehenderit in voluptate velit esse cillum dolore eu fugiat nulla pariatur. Excepteur sint occaecat cupidatat non proident, sunt in culpa qui officia deserunt mollit anim id est laborum.</p>
  </div>

  <!-- topics -->
  <h2 class="abs section-title" style="top:624px"><strong>Our Speaking</strong> Topics</h2>
  <div class="abs section-rule" style="top:646px"></div>

  <div class="abs card card-light" style="left:293px; top:691px; width:273px; height:127px; padding-top:25px">
    <h4>HEALTHY &amp; HAPPY</h4>
    <p style="margin-top:7px">PREVENT BURNOUT AND DEPRESSION<br>AND BUILD BETTER MENTAL HEALTH</p>
  </div>
  <div class="abs card card-dark" style="left:36px; top:674px; width:257px; height:164px; padding-top:30px">
    <h4>LIVE WELL</h4>
    <p style="margin-top:34px">MANAGE STRESS, PREVENT BURNOUT<br>&amp; LIVE A RESILIENT LIFE</p>
  </div>

  <div class="abs card card-light" style="left:36px; top:877px; width:274px; height:127px; padding-top:25px">
    <h4>MINDFUL LEADERSHIP</h4>
    <p style="margin-top:7px">MAXIMIZE ENGAGEMENT AND THRIVE<br>IN WORK AND LIFE</p>
  </div>
  <div class="abs card card-dark" style="left:309px; top:859px; width:257px; height:164px; padding-top:30px">
    <h4>LIVED EXPERIENCE</h4>
    <p style="margin-top:34px">PROVIDER BURNOUT &amp; THE ROLE OF<br>SELF-CARE</p>
  </div>

  <!-- video -->
  <div class="abs video-band"></div>
  <div class="abs outline-left"></div>
  <div class="abs outline-right"></div>
  <div class="abs video-frame"></div>
  <div class="abs video-still" role="img" aria-label="Video still of Dr. Ostrander seated at his office desk"></div>
  <svg class="abs play" viewBox="0 0 46 46" aria-hidden="true">
    <circle cx="23" cy="23" r="21" fill="none" stroke="#fff" stroke-width="3"/>
    <path d="M18 13 L33 23 L18 33 Z" fill="#fff"/>
  </svg>
  <svg class="abs arrow" style="left:128px" viewBox="0 0 16 24" aria-hidden="true"><path d="M12 2 L3 12 L12 22" fill="none" stroke="#fff" stroke-width="2.2"/></svg>
  <svg class="abs arrow" style="left:459px" viewBox="0 0 16 24" aria-hidden="true"><path d="M4 2 L13 12 L4 22" fill="none" stroke="#fff" stroke-width="2.2"/></svg>

</div>
</body>
</html>
```